I'm a one-man show, working as management consultant, project manager and offering personal coaching .
The logo should contain my name, and "management consultant" as a subtitle. My aim is to appear professional and kind of exclusive, but in a "casual" and dynamic way.
My aim is to implement new ideas in a holistic approach.
The colours preferred are black and shades of blue and violet, on a white background.

Contact Information for Business Card

I would like to have a white front, and a creative backside.
it would be awesome it the logo itself can be minted / stamped.

Besides my name, the business card should contain my operations, meaning
management consultant
project management
personal coaching

Logo Text

Matthias Dornhof - Management Consultant

Colors
886aae
0456a4
ffffff
33a6d7

Requirements
Must have
• a creative and catchy logo
• I would appreciate the profile of an eagle as a small symbol besides my name at the logo

```html
<!DOCTYPE html>
<html lang="en">
<head>
<meta charset="utf-8">
<title>Matthias Dornhof – Business Card</title>
<link rel="stylesheet" href="https://fonts.googleapis.com/css2?family=Roboto:wght@300;400;500;700&display=swap">
<style>
  :root {
    --stage: #e9e9ec;
    --card-white: #ffffff;
    --card-black: #222224;
    --ink: #1f1f22;
    --ink-soft: #55565b;
    --violet: #886aae;
    --blue: #0456a4;
    --sky: #33a6d7;
    --paper-light: #f4f4f6;
  }
  * { box-sizing: border-box; margin: 0; padding: 0; }
  html, body {
    width: 1200px;
    height: 1000px;
    overflow: hidden;
  }
  body {
    background: var(--stage);
    font-family: "Roboto", Arial, sans-serif;
    display: flex;
    align-items: center;
    justify-content: center;
    gap: 60px;
  }
  .card {
    width: 525px;
    height: 300px;
    border-radius: 4px;
    box-shadow: 0 10px 30px rgba(0,0,0,.18);
    position: relative;
    overflow: hidden;
  }
  .card--front {
    background: var(--card-white);
    color: var(--ink);
    padding: 34px 38px;
  }
  .card--back {
    background: var(--card-black);
    color: var(--paper-light);
    display: flex;
    align-items: center;
    justify-content: center;
  }
  .brand {
    display: flex;
    align-items: center;
    gap: 12px;
  }
  .brand__dot {
    width: 40px;
    height: 40px;
    border-radius: 50%;
    background: var(--violet);
    flex: none;
  }
  .brand__text { line-height: 1; }
  .brand__name {
    font-size: 19px;
    font-weight: 400;
    letter-spacing: .04em;
    text-transform: uppercase;
    line-height: 1.05;
  }
  .brand__subtitle {
    font-size: 9px;
    font-weight: 400;
    margin-top: 4px;
  }
  .card--front .brand__name { color: var(--ink); }
  .card--front .brand__subtitle { color: var(--ink-soft); }
  .card--back .brand__dot { width: 54px; height: 54px; }
  .card--back .brand__name { font-size: 24px; color: var(--paper-light); }
  .card--back .brand__subtitle { font-size: 11px; color: var(--paper-light); }

  .holder { margin-top: 26px; }
  .holder__name {
    font-size: 21px;
    font-weight: 700;
  }
  .holder__role {
    font-size: 12px;
    font-weight: 400;
    color: var(--ink-soft);
    margin-top: 6px;
  }
  .contact {
    list-style: none;
    margin-top: 18px;
    font-size: 12px;
    color: var(--ink-soft);
    line-height: 1.65;
  }
</style>
</head>
<body>
  <section class="card card--front" aria-label="Business card front">
    <div class="brand">
      <span class="brand__dot"></span>
      <div class="brand__text">
        <div class="brand__name">Matthias<br>Dornhof</div>
        <div class="brand__subtitle">Management Consultant</div>
      </div>
    </div>
    <div class="holder">
      <div class="holder__name">Mag. (FH) Matthias Dornhof</div>
      <div class="holder__role">Management Consultant</div>
    </div>
    <ul class="contact">
      <li>Mobile: +43 660 4817352</li>
      <li>Address: Birkenweg 9, 4821 Talheim</li>
      <li>Email: matthias@dornhof.co</li>
    </ul>
  </section>

  <section class="card card--back" aria-label="Business card back">
    <div class="brand">
      <span class="brand__dot"></span>
      <div class="brand__text">
        <div class="brand__name">Matthias<br>Dornhof</div>
        <div class="brand__subtitle">Management Consultant</div>
      </div>
    </div>
  </section>
</body>
</html>
```